Postcard Design

We are a full service lawn maintenace and landscapig company. Everything from maintenance, fertilizer programs, to design and install.
I would like the card to have a classy look including our logo which is attached. The logo would just have to contain the lettering and the swooshes not the pine tree background if not needed.

```html
<!DOCTYPE html>
<html lang="en">
<head>
<meta charset="utf-8">
<title>Silver Ridge Landscaping Postcard</title>
<link href="https://fonts.googleapis.com/css2?family=Source+Sans+3:wght@400;600;700&display=swap" rel="stylesheet">
<style>
  :root {
    --stage: #ecebe6;
    --green-dark: #5a8a34;
    --green-light: #8cc63f;
    --green-deep: #2f5f1e;
    --white: #ffffff;
    --grey-line: #9a9a9a;
    --placeholder: #a9c48c;
    --placeholder-soft: #bcd2a3;
  }
  * { margin: 0; padding: 0; box-sizing: border-box; }
  html, body { width: 815px; height: 1200px; overflow: hidden; }
  body {
    background: var(--stage);
    font-family: "Source Sans 3", "Helvetica Neue", Arial, sans-serif;
    position: relative;
  }
  .card {
    position: absolute;
    overflow: hidden;
    background: var(--white);
    box-shadow: 0 4px 10px rgba(0,0,0,0.25);
  }
  .card-front { left: 98px; top: 66px; width: 660px; height: 474px; }
  .card-back { left: 98px; top: 622px; width: 655px; height: 472px; }
  .card-shapes { position: absolute; inset: 0; }
  .photo {
    position: absolute; left: 0; top: 0;
    background: linear-gradient(180deg, var(--placeholder-soft) 0%, var(--placeholder) 100%);
  }
  .photo-garden { width: 660px; height: 380px; }
  .photo-mower { width: 655px; height: 240px; }

  .estimate { position: absolute; left: 39px; top: 398px; color: var(--white); }
  .estimate-label { font-size: 20px; font-weight: 600; line-height: 24px; }
  .estimate-phone {
    display: flex; align-items: center; gap: 16px;
    font-size: 25px; font-weight: 700; line-height: 30px;
  }
  .icon { width: 20px; height: 20px; flex: none; }
  .brand-name {
    position: absolute; right: 30px; top: 400px;
    color: var(--white); font-weight: 700; font-size: 25px;
    line-height: 26px; letter-spacing: 1px; text-align: center;
    text-transform: uppercase;
  }

  .about { position: absolute; left: 28px; top: 256px; width: 350px; color: var(--white); }
  .about-lead {
    font-size: 16px; line-height: 23px; letter-spacing: 0.5px;
    text-transform: uppercase; white-space: nowrap;
  }
  .about-lead strong { color: var(--green-deep); font-weight: 700; }
  .about-detail { margin-top: 8px; font-size: 17px; line-height: 23px; white-space: nowrap; }
  .about-detail strong { font-weight: 700; }

  .offer-box {
    position: absolute; left: 410px; top: 251px; width: 191px; height: 97px;
    background: var(--white); border: 1.5px dashed var(--green-dark); border-radius: 5px;
    color: var(--green-dark); text-align: center; font-weight: 700;
    font-size: 15px; line-height: 21px; padding-top: 11px;
  }
  .offer-box .offer-note { margin-top: 10px; font-weight: 600; }

  .contact { position: absolute; left: 327px; top: 410px; color: var(--green-deep); }
  .contact-row {
    display: flex; align-items: center; gap: 10px;
    font-size: 19px; font-weight: 700; line-height: 26px;
  }
  .contact-row .icon { width: 18px; height: 18px; }
</style>
</head>
<body>

<section class="card card-front">
  <div class="photo photo-garden" role="img" aria-label="Photo placeholder: manicured garden lawn with patio furniture and flowering shrubs"></div>
  <svg class="card-shapes" viewBox="0 0 660 474" width="660" height="474" aria-hidden="true">
    <path d="M0,318 C210,360 430,345 660,292 L660,474 L0,474 Z" fill="var(--green-light)"/>
    <path d="M0,324 C210,366 430,352 660,305 L660,474 L0,474 Z" fill="var(--white)"/>
    <path d="M0,334 C210,378 430,364 660,318 L660,474 L0,474 Z" fill="var(--green-dark)"/>
  </svg>
  <div class="estimate">
    <p class="estimate-label">Call for a free estimate</p>
    <p class="estimate-phone">
      <svg class="icon" viewBox="0 0 20 20" aria-hidden="true"><path d="M2,7 C2,3 18,3 18,7 L15,8 L14,6 C11,5 9,5 6,6 L5,8 Z M5,10 L15,10 L17,17 L3,17 Z" fill="currentColor"/><circle cx="10" cy="13.5" r="2" fill="var(--green-dark)"/></svg>
      555-014-2278
    </p>
  </div>
  <p class="brand-name">Silver Ridge<br>Landscaping</p>
</section>

<section class="card card-back">
  <div class="photo photo-mower" role="img" aria-label="Photo placeholder: commercial ride-on lawn mower on a freshly cut lawn"></div>
  <svg class="card-shapes" viewBox="0 0 655 472" width="655" height="472" aria-hidden="true">
    <path d="M0,212 C210,160 430,150 655,176 L655,472 L0,472 Z" fill="var(--green-light)"/>
    <path d="M0,220 C210,172 430,164 655,190 L655,472 L0,472 Z" fill="var(--white)"/>
    <path d="M0,230 C210,186 430,178 655,204 L655,472 L0,472 Z" fill="var(--green-dark)"/>
    <path d="M0,414 C160,392 330,388 655,380 L655,472 L0,472 Z" fill="var(--green-light)"/>
    <path d="M0,424 C160,402 330,398 655,392 L655,472 L0,472 Z" fill="var(--grey-line)"/>
    <path d="M0,428 C160,406 330,402 655,396 L655,472 L0,472 Z" fill="var(--white)"/>
  </svg>
  <div class="about">
    <p class="about-lead">We are a <strong>full service</strong> residential<br>and commercial&nbsp; lawn maintenace<br>and landscaping company.</p>
    <p class="about-detail">Our offer covers everything you need, from<br><strong>maintenance, fertilizer programs,</strong> to<br><strong>design</strong> and <strong>install</strong>.</p>
  </div>
  <div class="offer-box">
    <p>FREE LAWN ANALYSIS<br>AND CONSULTATION</p>
    <p class="offer-note">WITH THIS CARD</p>
  </div>
  <div class="contact">
    <p class="contact-row">
      <svg class="icon" viewBox="0 0 20 20" aria-hidden="true"><path d="M2,7 C2,3 18,3 18,7 L15,8 L14,6 C11,5 9,5 6,6 L5,8 Z M5,10 L15,10 L17,17 L3,17 Z" fill="currentColor"/><circle cx="10" cy="13.5" r="2" fill="var(--white)"/></svg>
      555-014-2278
    </p>
    <p class="contact-row">
      <svg class="icon" viewBox="0 0 20 20" aria-hidden="true"><rect x="2" y="5" width="16" height="11" fill="currentColor"/><path d="M2.5,5.5 L10,11 L17.5,5.5" fill="none" stroke="var(--white)" stroke-width="1.4"/></svg>
      hello@silverridgelawn.com
    </p>
  </div>
</section>

</body>
</html>
```